New Business Card Design Project

I would like my card design to look exactly like the logo, design, layout, and print of the current attached file. The only change I would like made would be for the print to say THE KMR GROUP instead of THE MORALES GROUP. Basically, just replace his group name with my group name. I would also like the backgroud to be the same texture and color as the attached file. I love the dark blue lettering and house logo on the card.

I am completely open to the rest of the card design. I just want something clean and simple. Only basic contact info required on the card. Maybe just name: Wade K Holmer and cell # 555.014.2289 and email wade@thepxbroker.com

```html
<!DOCTYPE html>
<html lang="en">
<head>
<meta charset="utf-8">
<title>THE KMR GROUP – Business Card</title>
<link href="https://fonts.googleapis.com/css2?family=Bebas+Neue&family=Lato:wght@400&display=swap" rel="stylesheet">
<style>
  :root {
    --navy: #2b2d7c;
    --paper: #f8f8f8;
    --paper-edge: #f1f1f2;
    --backdrop: #2c2c2e;
  }
  html, body {
    margin: 0;
    width: 1200px;
    height: 1200px;
    overflow: hidden;
    background: var(--backdrop);
  }
  .card {
    position: absolute;
    left: 193px;
    width: 814px;
    height: 466px;
    box-sizing: border-box;
    border: 28px solid var(--navy);
    background: radial-gradient(circle at 40% 35%, var(--paper), var(--paper-edge));
    color: var(--navy);
    font-family: "Lato", sans-serif;
  }
  .card--front { top: 74px; }
  .card--back  { top: 658px; }

  .brand {
    position: absolute;
    display: flex;
    flex-direction: column;
    align-items: center;
  }
  .brand__square { background: var(--navy); }
  .brand__name { white-space: nowrap; line-height: 1; }

  .card--front .brand { left: 0; width: 388px; top: 138px; }
  .card--front .brand__square { width: 70px; height: 70px; margin-bottom: 28px; }
  .card--front .brand__name { font-size: 42px; }

  .card--back .brand { left: 0; right: 0; top: 94px; }
  .card--back .brand__square { width: 110px; height: 110px; margin-bottom: 34px; }
  .card--back .brand__name { font-size: 60px; }

  .contact {
    position: absolute;
    left: 415px;
    top: 118px;
  }
  .contact__name {
    font-family: "Bebas Neue", sans-serif;
    font-size: 52px;
    line-height: 1;
    letter-spacing: 1px;
    margin: 0;
  }
  .contact__title {
    font-size: 21px;
    margin: 10px 0 26px;
  }
  .contact__row {
    display: flex;
    align-items: center;
    font-size: 22px;
    margin-bottom: 18px;
  }
  .contact__label {
    width: 23px;
    height: 23px;
    background: var(--navy);
    color: var(--paper);
    font-size: 17px;
    display: flex;
    align-items: center;
    justify-content: center;
    margin-right: 26px;
  }
  .contact__row--email .contact__label { margin-right: 32px; }
</style>
</head>
<body>
  <section class="card card--front">
    <div class="brand">
      <div class="brand__square"></div>
      <div class="brand__name">THE KMR GROUP</div>
    </div>
    <div class="contact">
      <h1 class="contact__name">WADE K HOLMER</h1>
      <div class="contact__title">MANAGER</div>
      <div class="contact__row"><span class="contact__label">P</span>+555 - 014 - 2289</div>
      <div class="contact__row contact__row--email"><span class="contact__label">E</span>wade@thepxbroker.com</div>
    </div>
  </section>

  <section class="card card--back">
    <div class="brand">
      <div class="brand__square"></div>
      <div class="brand__name">THE KMR GROUP</div>
    </div>
  </section>
</body>
</html>
```